Online Course Web Pages

Seeking web designer to design a 3 page website related to the promotion of an online course and a square graphic for the student login portal. Pages to include:
1) Opt-in page to request information on online course
2) Online course sales page with enrollment order form
3) Online course enrollment confirmation page
4) Online course login portal page design-- requires 600 x 600 graphic design
TARGET AUDIENCE: (for stock photo reference)
- Entry-level employees: Front-desk staff, servers, housekeeping staff, etc.
- Mid-level managers: Assistant managers, supervisors, department heads
- Experienced professionals: General managers, directors, executives
- Students: Hospitality, tourism, and leisure management students
- Recent graduates: Seeking entry-level positions in the industry
- Career changers: Individuals looking to transition into the hospitality, tourism, and leisure industry
- Hotel and accommodation professionals: General managers, hotel managers, front office managers, sales managers, revenue managers
- Restaurant and food service professionals: General managers, executive chefs, food and beverage directors, sommeliers
- Event planners and managers
- Tour operators and travel agents
- Spa and wellness professionals
- Customer service representatives
PRIMARY BRAND COLORS:
BACKGROUND - HEX CODE #FFDE59; TEXT - #000000; ACCENT #FFFFFF
COMPLEMENTARY COLORS (highlighter style colors)
sky #72EEFF; lime #C1FF72; stop sign #FF0000
DESIGN INSTRUCTIONS:
Webpages should incorporate the color palette used in the Ambrivo logo. Design tone should be fun, upbeat and modern. Stock images of happy workers and professionals throughout the hospitality, leisure and tourism industries should be incorporated throughout. Related stock images showing people or related items in the colors used in the logo are preferred. See sample web design, logo and web copy attached for additional reference.
ATTACHED FILES:
- Copy docs
- Logo
- Sample web page designs for optional reference
Updates
PROJECT ADJUSTMENT: I am seeking assistance with designing web pages to promote an online course. I am changing my original request for 4 web pages to just 2 web pages. Please reference the web brief and copy originally submitted for assistance with this project. Relevant copy for web page designs include: Lead Magnet Web Page Copy-- https://files.quorvanta.com/doc/8Kx2LmPq7RtVw9Yz3BnC5DfGh1JsA4eUo6iXk0Ma/edit?share=open; and Sales Page web page copy-- https://files.quorvanta.com/doc/3Hn7TbWq2ZyXc5VmR8LpK4JdSf9GaE1uQo6iNt0B/edit?share=open.

```html
<!DOCTYPE html>
<html lang="en">
<head>
<meta charset="utf-8">
<title>Ambrivo – Online Course Lead Magnet</title>
<link rel="stylesheet" href="https://fonts.googleapis.com/css2?family=Barlow+Semi+Condensed:wght@400;500&family=Arimo:wght@400;700&display=swap">
<style>
:root{
  --backdrop:#d9d9d9;
  --page:#ffffff;
  --ink:#000000;
  --heading:#24244a;
  --body:#333333;
  --brand-yellow:#ffde59;
  --panel:#000000;
  --soft-grey:#f2f2f2;
  --white:#ffffff;
  --ph-warm:#ece4dc;
  --ph-red:#f3dedb;
  --ph-green:#e6ecdc;
  --ph-herb:#f1f5ee;
}
*{box-sizing:border-box;margin:0;padding:0}
html,body{width:1200px;height:3563px;overflow:hidden;background:var(--backdrop)}
body{font-family:"Arimo",Arial,sans-serif;color:var(--body);position:relative}
.page{position:absolute;left:141px;top:106px;width:918px;height:3346px;background:var(--page);overflow:hidden}
.abs{position:absolute}
.heading{font-family:"Barlow Semi Condensed","Arial Narrow",sans-serif;font-weight:500;color:var(--heading);text-align:center;line-height:1.12}
.copy{font-size:8.1px;line-height:1.75;text-align:center;color:var(--body)}
.btn{position:absolute;background:var(--brand-yellow);color:var(--ink);font-size:7.6px;font-weight:700;display:flex;align-items:center;justify-content:center;letter-spacing:.2px}
.photo{position:absolute}
/* header */
.brand{position:absolute;display:flex;align-items:center;gap:4px;font-family:"Barlow Semi Condensed",sans-serif;font-weight:500;font-size:12px;color:var(--ink)}
.brand-mark{width:12px;height:12px;background:var(--brand-yellow);border:2px solid var(--ink)}
.site-title{left:149px;top:22px;font-size:32px;text-align:left;white-space:nowrap}
/* form */
.lead-form{position:absolute;background:var(--panel);color:var(--white);padding:20px 36px 0 41px}
.lead-form h2{font-family:"Barlow Semi Condensed",sans-serif;font-weight:500;font-size:32px;line-height:1;margin-bottom:10px}
.lead-form .intro{font-size:7.4px;line-height:1.6;margin-bottom:12px}
.field{background:var(--white);color:#444;font-size:7px;height:29px;display:flex;align-items:center;padding-left:9px;margin-bottom:16px;border-radius:1px}
.field.select{justify-content:space-between;padding-right:10px}
.row{display:flex;gap:12px}
.row .field{flex:1}
.lead-form .note{font-size:7.2px;margin:-6px 0 10px}
.lead-form .submit{position:static;height:30px;margin-bottom:14px}
.lead-form .fine{font-size:6.6px;line-height:1.55}
/* program grid */
.focus-item{position:absolute;width:360px;height:139px}
.focus-item .thumb{position:absolute;left:0;top:0;width:123px;height:139px}
.focus-item h3{position:absolute;left:162px;top:34px;font-family:"Barlow Semi Condensed",sans-serif;font-weight:500;font-size:14px;color:var(--ink)}
.focus-item p{position:absolute;left:162px;top:58px;width:192px;font-size:7.6px;line-height:1.85;color:var(--body)}
/* audience list */
.audience{position:absolute;display:flex;gap:12px;width:200px;font-size:7.4px;line-height:1.85;color:var(--body)}
.audience svg{flex:none;width:20px;height:20px;margin-top:1px}
/* footer */
.copyright{position:absolute;right:88px;top:3325px;font-size:7.4px;color:var(--ink)}
</style>
</head>
<body>
<main class="page">

  <!-- Header -->
  <header>
    <div class="brand" style="left:76px;top:37px"><span class="brand-mark"></span>Ambrivo</div>
    <h1 class="heading abs site-title">Online Course Lead Magnet</h1>
    <div class="photo" role="img" aria-label="Fresh spring onions" style="left:686px;top:0;width:150px;height:79px;background:var(--ph-green)"></div>
  </header>

  <!-- Hero -->
  <section>
    <div class="photo" role="img" aria-label="Smiling couple cooking together in aprons" style="left:0;top:79px;width:488px;height:397px;background:linear-gradient(135deg,#e2ddd6,#a9b7c2 50%,#8a7767)"></div>
    <div class="photo" role="img" aria-label="Bright kitchen background" style="left:834px;top:79px;width:84px;height:397px;background:#efe9e1"></div>
    <form class="lead-form" style="left:488px;top:79px;width:346px;height:397px">
      <h2>Get Started!</h2>
      <p class="intro">Craving a thriving, high-paying career in hospitality, leisure, or<br>tourism? You're not alone.</p>
      <div class="field select"><span>Online Course Lead Magnet</span><span>&#8964;</span></div>
      <div class="row"><div class="field">First Name</div><div class="field">Last Name</div></div>
      <div class="field">Email</div>
      <div class="field">Phone</div>
      <p class="note">Craving a thriving, high-paying career in hospitality</p>
      <div class="btn submit">LEARN MORE</div>
      <p class="fine">Craving a thriving, high-paying career in hospitality, leisure, or tourism? You're not alone. With millions of new jobs on the horizon, opportunities in the hospitality industry have never been more promising.</p>
    </form>
  </section>

  <!-- Intro -->
  <section>
    <div class="photo" role="img" aria-label="Grilled steak with rosemary on a plate" style="left:0;top:566px;width:156px;height:250px;background:var(--ph-warm)"></div>
    <div class="photo" role="img" aria-label="Red chili peppers" style="left:770px;top:540px;width:148px;height:290px;background:var(--ph-red)"></div>
    <h2 class="heading abs" style="left:200px;width:518px;top:573px;font-size:30px">A Thriving Career In Hospitality, Leisure<br>&amp; Tourism Starts Here…#Ambrivo</h2>
    <p class="copy abs" style="left:182px;width:556px;top:655px">Craving a thriving, high-paying career in hospitality, leisure, or tourism? You're not alone. With millions of new jobs on the horizon, opportunities in the hospitality industry have never been more promising. High-paying roles in hotel management, event planning, and luxury travel services are set to generate six-figure incomes like never before. BUT DO YOU HAVE WHAT IT TAKES TO RISE TO THE TOP?</p>
    <p class="copy abs" style="left:182px;width:556px;top:721px">If not then #Ambrivo can help you get there.</p>
    <div class="btn" style="left:398px;top:759px;width:122px;height:30px">REQUEST INFORMATION</div>
  </section>

  <!-- Chef banner -->
  <div class="photo" role="img" aria-label="Cheerful chef surrounded by flying vegetables" style="left:79px;top:874px;width:755px;height:313px;background:linear-gradient(180deg,#6e6b6b,#4a4646)"></div>
  <div class="photo" role="img" aria-label="Whole avocado" style="left:834px;top:1100px;width:84px;height:175px;background:var(--ph-green)"></div>

  <!-- Secret weapon -->
  <section>
    <div class="photo" role="img" aria-label="Grilled steak with herbs" style="left:0;top:1146px;width:140px;height:270px;background:var(--ph-warm)"></div>
    <div class="photo" role="img" aria-label="Avocado slices" style="left:820px;top:1340px;width:98px;height:220px;background:var(--ph-green)"></div>
    <h2 class="heading abs" style="left:200px;width:518px;top:1249px;font-size:30px">#Ambrivo Is Your Secret Weapon To<br>WIN-WIN-WIN No Matter What!</h2>
    <p class="copy abs" style="left:165px;width:590px;top:1338px">#Ambrivo is your comprehensive online program designed to propel your career in hospitality, leisure, or tourism. From crafting the perfect resume to mastering leadership skills, we'll equip you with the tools to excel. Our program empowers you to not only survive but thrive in this dynamic industry. With 50 years of experience and a proven track record of success, #Ambrivo has helped more than 500 professionals achieve higher salaries, prestigious job titles, and fulfilling careers. A well-defined career path isn't just about job satisfaction – it's about building a life you love. Let us help you achieve your full potential and career dreams.</p>
    <p class="copy abs" style="left:165px;width:590px;top:1414px">#Ambrivo is your comprehensive online program designed to propel your career in hospitality, leisure, or tourism. From crafting the perfect resume to mastering leadership skills, we'll equip you with the tools to excel. Our program empowers you to not only survive but thrive in this dynamic industry.</p>
  </section>

  <!-- Program focus -->
  <section>
    <h2 class="heading abs" style="left:200px;width:518px;top:1536px;font-size:30px">Our Program Focuses On</h2>
    <div class="photo" role="img" aria-label="Halved avocado with pit" style="left:834px;top:1640px;width:84px;height:160px;background:var(--ph-green)"></div>
    <div class="focus-item" style="left:79px;top:1599px">
      <div class="thumb" role="img" aria-label="Chef plating a dish" style="background:#b9a794"></div>
      <h3>Mastering Customer Service</h3>
      <p>Gain advanced skills to enhance guest experiences and build lasting relationships with our culturally relevant training, which transforms everyday tasks into exceptional interactions.</p>
    </div>
    <div class="focus-item" style="left:481px;top:1599px">
      <div class="thumb" role="img" aria-label="Plated rack of lamb" style="background:#d8c6b2"></div>
      <h3>Achieving Higher Salaries</h3>
      <p>Reach your earning potential with targeted career development strategies.</p>
    </div>
    <div class="focus-item" style="left:79px;top:1770px">
      <div class="thumb" role="img" aria-label="Hands slicing salmon" style="background:#8a7060"></div>
      <h3>Securing Better Job Titles</h3>
      <p>Position yourself for roles that reflect your skills and ambitions.</p>
    </div>
    <div class="focus-item" style="left:481px;top:1770px">
      <div class="thumb" role="img" aria-label="Dessert being drizzled with sauce" style="background:#e8d3a4"></div>
      <h3>Making A Lasting Impact</h3>
      <p>Making a Lasting Impact: Transform your work into a meaningful mission within the industry.</p>
    </div>
    <div class="btn" style="left:387px;top:1946px;width:145px;height:30px">REQUEST INFORMATION</div>
  </section>

  <!-- Career chance -->
  <section>
    <div class="photo" role="img" aria-label="Scattered herbs, peppercorns and garlic" style="left:0;top:2060px;width:918px;height:200px;background:var(--ph-herb)"></div>
    <div class="photo" role="img" aria-label="Scattered herbs, berries and garlic" style="left:0;top:2465px;width:918px;height:140px;background:var(--ph-herb)"></div>
    <div class="abs" style="left:79px;top:2153px;width:752px;height:312px;background:var(--soft-grey)"></div>
    <h2 class="heading abs" style="left:200px;width:518px;top:2216px;font-size:30px">Don't Leave Your Career To Chance</h2>
    <p class="copy abs" style="left:196px;width:526px;top:2272px;font-size:7.9px">In the competitive fields of hospitality, leisure, and tourism, mastering customer service is crucial for career advancement. Without top-notch training, your growth could be left to chance. Limited skills in this area can stifle progress, increase job insecurity, and lead to missed opportunities. Our #Ambrivo program ensures you not only navigate but excel in your career by focusing on customer service mastery—an indispensable skillset that can't be overlooked or underdeveloped. If you've felt stuck, underpaid, or uncertain about your next move, #Ambrivo will equip you with the expertise to secure the career success you deserve.</p>
    <div class="btn" style="left:387px;top:2368px;width:145px;height:30px">REQUEST INFORMATION</div>
  </section>

  <!-- Audience -->
  <section>
    <h2 class="heading abs" style="left:200px;width:518px;top:2588px;font-size:30px">Who Is #Ambrivo For?</h2>
    <div class="audience" style="left:223px;top:2664px">
      <svg viewBox="0 0 20 20" fill="none" stroke="#222" stroke-width="1.2"><path d="M3 12v-2a7 7 0 0 1 14 0v2"/><rect x="2" y="11" width="3.5" height="5" rx="1"/><rect x="14.5" y="11" width="3.5" height="5" rx="1"/></svg>
      <span>Aspiring Customer Service Professionals in Hospitality, Leisure, and Tourism</span>
    </div>
    <div class="audience" style="left:482px;top:2664px;width:230px">
      <svg viewBox="0 0 20 20" fill="none" stroke="#222" stroke-width="1.2"><path d="M5 12a3.5 3.5 0 0 1 1-7 4 4 0 0 1 8 0 3.5 3.5 0 0 1 1 7z"/><path d="M5.5 12v4h9v-4"/></svg>
      <span>Entry-Level Professionals (Students, Young Adults, Returning Citizens, etc.)</span>
    </div>
    <div class="audience" style="left:223px;top:2729px">
      <svg viewBox="0 0 20 20" fill="none" stroke="#222" stroke-width="1.2"><path d="M4 16l2-5 8-8 3 3-8 8z"/><path d="M4 16l3-1"/></svg>
      <span>Mid-Career Professionals Seeking a Career Transition</span>
    </div>
    <div class="audience" style="left:482px;top:2729px">
      <svg viewBox="0 0 20 20" fill="none" stroke="#222" stroke-width="1.2"><rect x="4" y="5" width="12" height="8" rx="1"/><path d="M2 15h16"/></svg>
      <span>Business Organizations Seeking Training for Their Teams</span>
    </div>
  </section>

  <!-- Bottom sign-up -->
  <section>
    <div class="photo" role="img" aria-label="Professional kitchen with stacked pans" style="left:0;top:2854px;width:76px;height:397px;background:#a9a49e"></div>
    <form class="lead-form" style="left:76px;top:2854px;width:347px;height:397px">
      <h2>Get Started!</h2>
      <p class="intro">Craving a thriving, high-paying career in hospitality, leisure, or<br>tourism? You're not alone.</p>
      <div class="field select"><span>Online Course Lead Magnet</span><span>&#8964;</span></div>
      <div class="row"><div class="field">First Name</div><div class="field">Last Name</div></div>
      <div class="field">Email</div>
      <div class="field">Phone</div>
      <p class="note">Craving a thriving, high-paying career in hospitality</p>
      <div class="btn submit">LEARN MORE</div>
      <p class="fine">Craving a thriving, high-paying career in hospitality, leisure, or tourism? You're not alone. With millions of new jobs on the horizon, opportunities in the hospitality industry have never been more promising.</p>
    </form>
    <div class="photo" role="img" aria-label="Two chefs reviewing a tablet in a kitchen" style="left:423px;top:2854px;width:495px;height:397px;background:linear-gradient(135deg,#b8ada2,#7a6a5c 60%,#5a4c40)"></div>
    <h2 class="abs" style="left:535px;top:3119px;font-family:'Barlow Semi Condensed',sans-serif;font-weight:500;font-size:29px;color:var(--white)">Who Is #Ambrivo For?</h2>
    <p class="abs" style="left:535px;top:3162px;width:310px;font-size:7.4px;line-height:1.75;color:var(--white)">Ready to advance your career and achieve success in the booming hospitality, leisure, and tourism industry? Complete the form below to discover how #Ambrivo can promote you to the top of the industry!</p>
  </section>

  <!-- Footer -->
  <footer>
    <div class="brand" style="left:76px;top:3318px"><span class="brand-mark"></span>Ambrivo</div>
    <p class="copyright">© 2024 #Ambrivo. All rights reserved.</p>
  </footer>

</main>
</body>
</html>
```